Equipment Finance Specialist I work with companies who need the funds to buy their equipment

I would like a business card that stands out on the shelves. I want to be able to hand it to someone and say WOW. This card should have my logo.
You can put color into it I am very open on design and color

What my company does is we deal with dealerships that sell equipment such as Dump Trucks garbage trucks tractors trailers. Customers get referred to us and depending on their time in business we will ask for the following items

Companies that have been in business for more than two years we have a credit application program up to 250K . With this program we need the following items Credit application filled out(which is what I would like to be able for the customer to click on my website to get.) as well as three current month bank statements.

Deals over 250k we will need the following items

2 years business tax returns
2 years personal tax returns
Profit & Loss statement
Personal Financial Statement

what we do
100% FINANCING
SEASONAL PAYMENTS
LOAN BALLOON PAYMENTS
TRAC LEASING
LOW-INTEREST REFINANCING RATES
DEBT CONSOLIDATION

We specialize in creative financing solutions and offer a variety of reliable, flexible and expandable lending choices.

Target Market(s)

Trucking Companies

Industry/Entity Type

Trucking Company

Contact Information for Business Card

* $250,000 Application only Program
* Loans from $30,000 to 5,000,000
* Competitive Interest Rates

Font styles to use
Serif
Sans Serif

Colors

Designer to choose colors to be used in the design.

Requirements
Must have
• On the back of the card.
• * $250,000 Application only Program
• * Loans from $30,000 to 5,000,000
• My name, email, website. address
• * Competitive Interest Rates
• * 100% Financing
Nice to have
• I want my logo to pop on the card
• My logo is the great one I would like to use
Should not have
• I am up for your creativity as well

```html
<!DOCTYPE html>
<html lang="en">
<head>
<meta charset="utf-8">
<title>Ridgeline Funding – Business Card</title>
<link href="https://fonts.googleapis.com/css2?family=Montserrat:wght@700;800&family=Source+Sans+3:wght@400;600&display=swap" rel="stylesheet">
<style>
  :root {
    --navy: #0d2a78;
    --navy-deep: #0a1f5c;
    --navy-light: #1a44a8;
    --red: #d01c35;
    --paper: #ffffff;
    --ink: #3a3f4a;
    --ghost: #e3e8f1;
    --stage: #2b2d31;
  }
  * { margin: 0; padding: 0; box-sizing: border-box; }
  html, body {
    width: 1200px; height: 892px; overflow: hidden;
    background: var(--stage);
    font-family: "Source Sans 3", Arial, sans-serif;
  }
  .card {
    position: absolute;
    width: 560px; height: 320px;
    overflow: hidden;
    box-shadow: 0 14px 30px rgba(0,0,0,.45);
  }
  /* Back of card */
  .card-back {
    left: 60px; top: 100px;
    background: linear-gradient(160deg, var(--navy-light) 0%, var(--navy) 50%, var(--navy-deep) 100%);
    color: var(--paper);
  }
  .back-brand {
    position: absolute; left: 0; right: 0; top: 78px;
    display: flex; flex-direction: column; align-items: center; gap: 12px;
  }
  .brand-dot {
    width: 86px; height: 86px; border-radius: 50%;
    background: var(--paper);
  }
  .back-brand .brand-name {
    font-family: "Montserrat", Arial, sans-serif;
    font-weight: 800; font-size: 22px; letter-spacing: 2px;
    color: var(--paper);
  }
  .back-offers {
    position: absolute; left: 0; right: 0; bottom: 34px;
    text-align: center; font-size: 15px; line-height: 1.35;
  }
  .back-offers .sep { margin: 0 5px; }

  /* Front of card */
  .card-front {
    left: 580px; top: 470px;
    background: var(--paper);
  }
  .front-decoration {
    position: absolute; right: 30px; top: 0; width: 300px; height: 290px;
    background: radial-gradient(ellipse at 55% 45%, var(--ghost) 0%, rgba(227,232,241,.45) 55%, rgba(255,255,255,0) 75%);
  }
  .front-band-bottom {
    position: absolute; left: 0; right: 0; bottom: 0; height: 12px;
    background: var(--navy);
  }
  .front-band-right {
    position: absolute; right: 0; top: 0; bottom: 0; width: 8px;
    background: var(--navy);
  }
  .name-block {
    position: absolute; left: 0; top: 44px;
    padding-left: 30px;
    border-left: 8px solid var(--navy);
  }
  .person-name {
    font-family: "Montserrat", Arial, sans-serif;
    font-weight: 800; font-size: 21px; color: var(--navy);
    letter-spacing: .5px;
  }
  .person-title {
    font-size: 16px; color: var(--red); letter-spacing: .5px; line-height: 1.1;
  }
  .front-brand {
    position: absolute; right: 34px; top: 148px;
    display: flex; align-items: center; gap: 10px;
  }
  .front-brand .brand-dot { width: 52px; height: 52px; background: var(--navy); }
  .front-brand .brand-name {
    font-family: "Montserrat", Arial, sans-serif;
    font-weight: 800; font-size: 20px; line-height: 1.05;
    color: var(--navy); letter-spacing: 1px;
  }
  .contact {
    position: absolute; left: 38px; bottom: 34px;
    font-size: 15px; color: var(--ink); line-height: 1.3;
  }
  .address { margin-bottom: 8px; }
  .contact-row { display: flex; align-items: center; gap: 10px; }
  .contact-row svg { width: 14px; height: 14px; fill: var(--navy); flex: none; }
</style>
</head>
<body>

<section class="card card-back" aria-label="Card back">
  <div class="back-brand">
    <span class="brand-dot"></span>
    <span class="brand-name">RIDGELINE FUNDING</span>
  </div>
  <p class="back-offers">
    $250,000 Application only Program<span class="sep">•</span>Loans from $30,000 to 5,000,000<br>
    Competitive Interest Rates<span class="sep">•</span>100% Financing
  </p>
</section>

<section class="card card-front" aria-label="Card front">
  <div class="front-decoration" role="img" aria-label="Faint large truck illustration in the background"></div>
  <div class="front-band-right"></div>
  <div class="front-band-bottom"></div>

  <div class="name-block">
    <h1 class="person-name">MARK HALDEN</h1>
    <p class="person-title">PRESIDENT</p>
  </div>

  <div class="front-brand">
    <span class="brand-dot"></span>
    <span class="brand-name">RIDGELINE<br>FUNDING</span>
  </div>

  <div class="contact">
    <p class="address">4120 Harbor Point Road<br>Lakeview, NY 11020</p>
    <p class="contact-row">
      <svg viewBox="0 0 16 16" aria-hidden="true"><path d="M3.5 1l2.5 3-1.5 1.5c.8 2 2.5 3.7 4.5 4.5L10.5 8.5l3 2.5-1.5 3C6.5 14 2 9.5 2 2.5z"/></svg>
      555 0142 7781
    </p>
    <p class="contact-row">
      <svg viewBox="0 0 16 16" aria-hidden="true"><path d="M1 3h14v10H1z M1.8 3.6L8 8.5l6.2-4.9" fill="none" stroke="#0d2a78" stroke-width="1.6"/></svg>
      mark@ridgelinefunding.com
    </p>
    <p class="contact-row">
      <svg viewBox="0 0 16 16" aria-hidden="true"><circle cx="8" cy="8" r="6.5" fill="none" stroke="#0d2a78" stroke-width="1.5"/><path d="M1.5 8h13M8 1.5c-3 3.5-3 9.5 0 13M8 1.5c3 3.5 3 9.5 0 13" fill="none" stroke="#0d2a78" stroke-width="1.2"/></svg>
      www.ridgelinefunding.com
    </p>
  </div>
</section>

</body>
</html>
```